Rack card for a integrative medical practice

Need an eye-catching rack card with our logo with content as provided. We have a membership based holistic medical practice which incorporates western and holistic medicine. We would like to focus on wellness and healthy lifestyle. See uploaded files for what is included in the membership. Would like 2 page rack card color on both sides. Logo must be on the front.

Target Market(s)

People looking for alternative medicine, healthy lifestyle.

Industry/Entity Type

Health and Wellness

Colors
00AB8E
00BBA5
67D7C9
C6EFE9
E9F9F6

Requirements
Must have
• Must spark interest at first sight. Clear message.
Nice to have
• Warm, bright and positive vibe. Organic, neutral and earthy colors.
Should not have
• Traditional medical practice vibe (cold, formal, industrial). No PINK except the logo.

```html
<!DOCTYPE html>
<html lang="en">
<head>
<meta charset="UTF-8">
<title>Sorrel Health &amp; Wellness – Rack Card</title>
<link href="https://fonts.googleapis.com/css2?family=Lora:wght@400;600;700&display=swap" rel="stylesheet">
<style>
  :root{
    --accent:#00ab8e;
    --accent-deep:#008f77;
    --accent-soft:#00bba5;
    --green:#0c5140;
    --ink:#34444b;
    --sky-top:#c6efe9;
    --sky-low:#e9f9f6;
    --paper:#ffffff;
    --stage:#4a4a4a;
  }
  *{box-sizing:border-box;margin:0;padding:0}
  html,body{width:900px;height:1200px;overflow:hidden}
  body{background:var(--stage);font-family:"Lora",Georgia,serif;position:relative}
  .card{position:absolute;top:197px;width:360px;height:805px;background:var(--paper);overflow:hidden;box-shadow:0 10px 30px rgba(0,0,0,.35)}
  .card--front{left:60px;background:linear-gradient(180deg,var(--sky-top) 0%,var(--sky-low) 60%,#fff 100%)}
  .card--back{left:480px;background:linear-gradient(180deg,#fff 0%,#fff 45%,#f4f7f5 75%,#fff 100%)}
  .card svg.shapes{position:absolute;left:0;top:0}
  .abs{position:absolute;left:0;width:100%;text-align:center}

  .front-title{top:38px}
  .front-title .line1{font-size:25px;color:var(--accent);letter-spacing:.5px}
  .front-title .line1 b{font-weight:700}
  .front-title .line2{font-size:40px;color:var(--ink);line-height:1.05;letter-spacing:.5px}
  .front-photo{position:absolute;left:20px;top:150px;width:320px;height:245px;border-radius:160px 160px 40px 40px;
    background:radial-gradient(ellipse at 55% 45%,#f4f6f8 0%,#c6d3e0 35%,#3c5a8a 75%,#1f3460 100%)}

  .brand{display:flex;align-items:center;justify-content:center;gap:8px}
  .brand .dot{width:14px;height:14px;border-radius:50%;background:var(--accent)}
  .brand .name{font-size:26px;letter-spacing:6px;color:var(--green);font-weight:400}
  .front-brand{top:420px}

  .front-pitch{top:580px;color:#fff}
  .front-pitch .lead{font-size:20px;letter-spacing:.5px}
  .front-pitch .sub{font-size:17px;line-height:1.2}
  .front-pitch .small{font-size:14px}

  .phone{display:inline-block;font-size:20px;padding:3px 22px;border-radius:16px}
  .phone--light{background:#fff;color:var(--green)}
  .phone--accent{background:var(--accent);color:#fff}
  .front-phone{top:676px}
  .address{font-size:8.5px;color:#444;line-height:1.4}
  .address-pos{top:779px}

  .back-brand{top:28px;flex-direction:column;gap:6px}
  .back-photo{position:absolute;left:0;top:125px;width:360px;height:280px;
    background:linear-gradient(180deg,#e8ecea 0%,#b7bfae 30%,#7b8a5f 50%,#9a5a3e 72%,#6f3d28 100%)}
  .member-pill{top:416px}
  .member-pill .pill{display:inline-block;border:2px solid var(--accent);border-radius:30px;padding:4px 26px;background:#fff}
  .member-pill .l1{font-size:21px;color:var(--green);font-weight:600}
  .member-pill .l2{font-size:22px;color:var(--accent);letter-spacing:1px}
  .benefits{position:absolute;left:30px;right:20px;top:504px;list-style:none}
  .benefits li{position:relative;padding-left:15px;font-size:10.5px;color:#222;line-height:1.25;margin-bottom:2px}
  .benefits li::before{content:"";position:absolute;left:2px;top:2px;width:4px;height:7px;border:solid var(--accent);border-width:0 1.6px 1.6px 0;transform:rotate(40deg)}
  .benefits .num{font-size:12.5px}
  .back-phone{top:688px}
</style>
</head>
<body>

<section class="card card--front">
  <div class="abs front-title">
    <div class="line1"><b>SORREL</b> HEALTH</div>
    <div class="line2">&amp;WELLNESS</div>
  </div>
  <div class="front-photo" role="img" aria-label="Photo of a doctor shaking hands with a patient"></div>
  <div class="abs brand front-brand"><span class="dot"></span><span class="name">SORREL</span></div>

  <svg class="shapes" width="360" height="805" viewBox="0 0 360 805" aria-hidden="true">
    <defs>
      <linearGradient id="accentBand" x1="0" y1="0" x2="0" y2="1">
        <stop offset="0" stop-color="#008f77"/><stop offset="1" stop-color="#00bba5"/>
      </linearGradient>
    </defs>
    <path d="M0,512 C70,512 125,500 155,478 Q180,458 180,448 Q180,458 205,478 C235,500 290,512 360,512 V805 H0Z" fill="#0c5140"/>
    <path d="M0,526 C70,526 125,514 155,492 Q180,472 180,462 Q180,472 205,492 C235,514 290,526 360,526 V805 H0Z" fill="url(#accentBand)"/>
    <path d="M0,758 Q180,690 360,758 V805 H0Z" fill="#0c5140"/>
    <path d="M0,772 Q180,708 360,772 V805 H0Z" fill="#fff"/>
  </svg>

  <div class="abs front-pitch">
    <div class="lead">A DIRECT PRIMARY CARE</div>
    <div class="sub">practice focused on a more holistic</div>
    <div class="small">and personal approach to medicine</div>
  </div>
  <div class="abs front-phone"><span class="phone phone--light">555-013-2740</span></div>
  <div class="abs address address-pos">1420 Orchard Ave. STE 2B Fairview, Indiana 46000<br>www.sorreltotalhealth.example</div>
</section>

<section class="card card--back">
  <div class="abs brand back-brand"><span class="dot"></span><span class="name">SORREL</span></div>
  <div class="back-photo" role="img" aria-label="Photo of a woman meditating on a red rock hilltop"></div>

  <svg class="shapes" width="360" height="805" viewBox="0 0 360 805" aria-hidden="true">
    <path d="M0,360 C70,362 125,352 155,334 Q180,318 180,308 Q180,318 205,334 C235,352 290,362 360,360 V805 H0Z" fill="#0c5140"/>
    <path d="M0,392 C70,392 125,382 155,364 Q180,348 180,340 Q180,348 205,364 C235,382 290,392 360,392 V805 H0Z" fill="#fff"/>
    <path d="M0,758 Q180,690 360,758 V805 H0Z" fill="#0c5140"/>
    <path d="M0,772 Q180,708 360,772 V805 H0Z" fill="#fff"/>
  </svg>

  <div class="abs member-pill">
    <div class="pill">
      <div class="l1">what's included in</div>
      <div class="l2">YOUR MEMBERSHIP</div>
    </div>
  </div>
  <ul class="benefits">
    <li>Unlimited office visits with no copay</li>
    <li>Direct communication with your doctor</li>
    <li>Discounted labs, imaging and medications</li>
    <li>Free initial acupuncture session <span class="num">($250 value)</span></li>
    <li>2 Vitascan testings per year <span class="num">($100 value)</span></li>
    <li>Discounts for supplements and health products in the clinic</li>
    <li>Discounts for iv vitamin infusion therapy</li>
    <li>Personalized nutrition plan after advanced testing such as gut microbiome, hormonal, metabolism</li>
  </ul>
  <div class="abs back-phone"><span class="phone phone--accent">555-013-2740</span></div>
  <div class="abs address address-pos">1420 Orchard Ave. STE 2B Fairview, Indiana 46000<br>www.sorreltotalhealth.example</div>
</section>

</body>
</html>
```